Kestrel Lane flyer

Need a A6 size horizontal layout flyer. See attached example for ideas as well as some images I have which you can use. we are a hire car company that provides vehicles to clients who have recently been involved in car accidents and who's cars are currently getting fixed and so they lose the use of their own vehicle. see our website to keep flyer in line with website and for any further information kestrellane.com.au

Target Market(s)

people involved in not at fault car accidents

Industry/Entity Type

It Company

Requirements
Must have
• *ask people to let us know where they got our flyer from when they call us
• *call to action for people to call our phone number 1800 417 582
Should not have
• any mentioning that the vehicle is free

```html
<!DOCTYPE html>
<html lang="en">
<head>
<meta charset="utf-8">
<title>Kestrel Lane Flyer</title>
<link rel="stylesheet" href="https://fonts.googleapis.com/css2?family=Roboto:ital,wght@0,300;0,400;0,500;0,700;0,900;1,700&family=Roboto+Condensed:wght@400;700&display=swap">
<style>
  :root {
    --page-bg: #93b9f4;
    --paper: #ffffff;
    --brand-blue: #4a8cf0;
    --step-yellow: #f4b73c;
    --step-light: #5b9df2;
    --step-dark: #3468d4;
    --navy: #10284f;
    --accent-yellow: #f6b531;
    --ink: #2b2f3a;
    --link-blue: #1f66d9;
    --arrow-blue: #2c5de8;
    --white: #ffffff;
  }
  * { box-sizing: border-box; margin: 0; padding: 0; }
  html, body { width: 1200px; height: 1015px; overflow: hidden; }
  body {
    background: var(--page-bg);
    font-family: "Roboto", Arial, sans-serif;
    position: relative;
  }
  .flyer {
    position: absolute;
    left: 50px; top: 117px;
    width: 1100px; height: 780px;
    background: var(--paper);
    overflow: hidden;
    box-shadow: 0 10px 30px rgba(20, 40, 90, .25);
  }
  .hero-photo {
    position: absolute; left: 0; top: 0;
    width: 1100px; height: 220px;
    background: linear-gradient(100deg, #1b2f5e 0%, #34579c 30%, #233f80 48%, #4f7fd0 70%, #2b4d97 100%);
  }
  .brand-banner {
    position: absolute; left: 300px; top: 105px;
    width: 500px; height: 195px;
    background: var(--brand-blue);
    clip-path: polygon(0 0, 100% 0, 82% 100%, 18% 100%);
    text-align: center;
    color: var(--white);
  }
  .brand-name {
    margin-top: 62px;
    font-size: 34px; font-weight: 700;
    letter-spacing: .5px;
  }
  .brand-tagline {
    margin-top: 8px;
    font-family: "Roboto Condensed", Arial, sans-serif;
    font-weight: 700; font-size: 17px; line-height: 1.1;
  }
  .owned-badge {
    position: absolute; left: 1010px; top: 150px;
    width: 44px; height: 44px; border-radius: 50%;
    background: var(--white); opacity: .9;
  }
  .headline {
    position: absolute; left: 0; top: 308px; width: 1100px;
    text-align: center;
    font-family: "Roboto Condensed", Arial, sans-serif;
    font-weight: 700; font-size: 22px; line-height: 1.12;
    color: var(--ink);
  }
  .headline .accent { color: var(--link-blue); }
  .lower-band {
    position: absolute; left: 0; top: 440px;
    width: 1100px; height: 285px;
    background: linear-gradient(180deg, #4f95f2 0%, #3b76ef 55%, #2a57ee 100%);
  }
  .steps {
    position: absolute; left: 40px; top: 375px;
    width: 640px; height: 140px;
    display: flex; justify-content: space-between; align-items: stretch;
  }
  .step {
    width: 186px; height: 140px;
    display: flex; flex-direction: column; align-items: center;
    padding-top: 14px;
    text-align: center;
    font-family: "Roboto Condensed", Arial, sans-serif;
    font-weight: 700; font-size: 13px; line-height: 1.25;
    box-shadow: 0 4px 10px rgba(0,0,0,.15);
  }
  .step-number { font-size: 22px; margin-bottom: 8px; }
  .step-icon { width: 22px; height: 22px; margin-bottom: 8px; }
  .step--call { background: var(--step-yellow); color: var(--ink); }
  .step--details { background: var(--step-light); color: var(--ink); }
  .step--vehicle { background: var(--step-dark); color: var(--white); }
  .step-phone { font-size: 15px; }
  .step-arrow { align-self: center; width: 20px; height: 26px; }
  .about {
    position: absolute; left: 40px; top: 532px;
    width: 640px; color: var(--white);
  }
  .about-title {
    text-align: center;
    font-family: "Roboto Condensed", Arial, sans-serif;
    font-weight: 700; font-size: 20px;
    color: var(--accent-yellow);
    margin-bottom: 6px;
  }
  .about-body {
    font-size: 12px; font-weight: 300; line-height: 1.35;
    text-align: justify;
  }
  .benefits {
    position: absolute; left: 720px; top: 375px;
    width: 340px; height: 330px;
    border: 14px solid var(--navy);
    padding: 18px 22px;
    background: linear-gradient(180deg, #3c7cef, #2d5ded);
  }
  .benefits-title {
    font-family: "Roboto Condensed", Arial, sans-serif;
    font-weight: 700; font-size: 21px; line-height: 1.05;
    color: var(--accent-yellow);
    text-align: center;
    margin-bottom: 14px;
  }
  .benefit-list { list-style: none; }
  .benefit {
    display: flex; align-items: flex-start; gap: 8px;
    color: var(--white);
    font-family: "Roboto Condensed", Arial, sans-serif;
    font-weight: 700; font-size: 19px; line-height: 1.02;
    margin-bottom: 9px;
  }
  .benefit svg { flex: none; width: 16px; height: 16px; margin-top: 2px; }
  .referral-note {
    margin-top: 12px;
    font-family: "Roboto Condensed", Arial, sans-serif;
    font-weight: 700; font-size: 14px; line-height: 1.2;
    color: var(--accent-yellow);
    text-align: center;
  }
  .footer {
    position: absolute; left: 0; top: 725px;
    width: 1100px; height: 55px;
    display: flex; justify-content: space-between; align-items: center;
    padding: 0 40px;
    font-weight: 700; font-style: italic; font-size: 17px;
    color: var(--ink);
  }
  .social { display: flex; align-items: center; gap: 8px; }
  .social-dot {
    width: 20px; height: 20px; border-radius: 50%;
    background: var(--ink);
  }
</style>
</head>
<body>
  <main class="flyer">
    <div class="hero-photo" role="img" aria-label="Photo of a silver car front beside a smiling couple seated in a car"></div>

    <div class="brand-banner">
      <div class="brand-name">Kestrel Lane</div>
      <div class="brand-tagline">AUSTRALIA'S NO.1 CAR ACCIDENT<br>REPLACEMENT SERVICE</div>
    </div>
    <div class="owned-badge" aria-hidden="true"></div>

    <h1 class="headline">ARRANGING AN ACCIDENT REPLACEMENT VEHICLE<br><span class="accent">FOR YOURSELF</span> IS EASY AS <span class="accent">1,2,3</span></h1>

    <div class="lower-band"></div>

    <section class="steps">
      <div class="step step--call">
        <div class="step-number">1</div>
        <svg class="step-icon" viewBox="0 0 24 24" fill="none" stroke="currentColor" stroke-width="1.6" stroke-linecap="round" stroke-linejoin="round"><path d="M5 3h3l2 5-2.5 1.5a11 11 0 0 0 7 7L16 14l5 2v3a2 2 0 0 1-2 2A16 16 0 0 1 3 5a2 2 0 0 1 2-2z"/></svg>
        <div>CALL US ON<br><span class="step-phone">1800 417 582</span><br>(FREE CALL)</div>
      </div>
      <svg class="step-arrow" viewBox="0 0 20 26" fill="none" stroke="var(--arrow-blue)" stroke-width="2.4"><path d="M6 4l9 9-9 9"/></svg>
      <div class="step step--details">
        <div class="step-number">2</div>
        <svg class="step-icon" viewBox="0 0 24 24" fill="none" stroke="currentColor" stroke-width="1.6" stroke-linecap="round" stroke-linejoin="round"><path d="M5 5h3l2 5-2.5 1.5a11 11 0 0 0 5 5L14 14l5 2v3a2 2 0 0 1-2 2A14 14 0 0 1 3 7a2 2 0 0 1 2-2z"/><path d="M14 3a7 7 0 0 1 7 7"/><path d="M14 7a3 3 0 0 1 3 3"/></svg>
        <div>PROVIDE ACCIDENT DETAILS</div>
      </div>
      <svg class="step-arrow" viewBox="0 0 20 26" fill="none" stroke="var(--arrow-blue)" stroke-width="2.4"><path d="M6 4l9 9-9 9"/></svg>
      <div class="step step--vehicle">
        <div class="step-number">3</div>
        <svg class="step-icon" viewBox="0 0 24 24" fill="none" stroke="currentColor" stroke-width="1.6" stroke-linecap="round" stroke-linejoin="round"><path d="M3 15v-3l2-5h14l2 5v3z"/><path d="M3 12h18"/><circle cx="7" cy="17" r="1.6"/><circle cx="17" cy="17" r="1.6"/></svg>
        <div>YOU GET A REPLACEMENT<br>VEHICLE<br>WE TAKE CARE OF THE REST</div>
      </div>
    </section>

    <section class="about">
      <h2 class="about-title">ABOUT US</h2>
      <p class="about-body">Throughout Australia, there are a lot of people on the roads, especially in the main cities like Sydney and Melbourne. It's not uncommon to get into a car accident. Whether it's a simple fender bender or something more severe, your car could end up in a repair shop for repairs. The biggest problem that you now have to deal with is that while your vehicle is in the repair shop, you have no car. If the accident wasn't your fault, an accident replacement vehicle is available to you. You can call and schedule this replacement car so that you are not left without a car while it is under repairs. You shouldn't be inconvenienced just because someone else caused an accident. Knowing how to get a rental car and what the benefits will help you immensely.</p>
    </section>

    <section class="benefits">
      <h2 class="benefits-title">WE GET YOUR BACK<br>ON THE ROAD TODAY</h2>
      <ul class="benefit-list">
        <li class="benefit"><svg viewBox="0 0 16 16" fill="none" stroke="#f6b531" stroke-width="1.6" stroke-linecap="round"><path d="M13 4.5A6.5 6.5 0 1 0 14.5 8"/><path d="M5 8l2.5 2.5L14 3"/></svg>Free Advice</li>
        <li class="benefit"><svg viewBox="0 0 16 16" fill="none" stroke="#f6b531" stroke-width="1.6" stroke-linecap="round"><path d="M13 4.5A6.5 6.5 0 1 0 14.5 8"/><path d="M5 8l2.5 2.5L14 3"/></svg>Excess Waiver<br>Included</li>
        <li class="benefit"><svg viewBox="0 0 16 16" fill="none" stroke="#f6b531" stroke-width="1.6" stroke-linecap="round"><path d="M13 4.5A6.5 6.5 0 1 0 14.5 8"/><path d="M5 8l2.5 2.5L14 3"/></svg>Free Delivery</li>
        <li class="benefit"><svg viewBox="0 0 16 16" fill="none" stroke="#f6b531" stroke-width="1.6" stroke-linecap="round"><path d="M13 4.5A6.5 6.5 0 1 0 14.5 8"/><path d="M5 8l2.5 2.5L14 3"/></svg>Late Models<br>New vehicles</li>
      </ul>
      <p class="referral-note">When you call, please tell us<br>where you got this flyer!</p>
    </section>

    <footer class="footer">
      <span class="website">www.kestrellane.com.au</span>
      <span class="social">Follow us on : <span class="social-dot"></span><span class="social-dot"></span></span>
    </footer>
  </main>
</body>
</html>
```